Asian Pakistani: Wedding Invitation

Design a pakistani asian wedding invitation.
Islamic theme, with arabic text:

Text to be used:

Start with: bismillah and dua for marriage. (The Holy Quran chapter 25 verse 75 with arabic text and english translation below)

Mrs. Rubina Sohail wife of (late) Mr. Sohail Imran Qureshi
Cordially requests your company to grace the joyous occasion of the wedding of their beloved daughter
Mehreen Qureshi
Daughter of ( late) Mr Sohail Imran qureshi
with
Bilal Siddiqui
Son of Mr. Junaid Siddiqui & Mrs Shazia Siddiqui

Insha’Allah on Thursday 29th August 2019 at Velvet Orchard
12 Marlow Crescent, Croydon
CR7 2LP
Baraat Arrival 6:30

RSVP
Usman Qureshi 07700 900412
Tariq Mehmood 07700 900583
Faisal Butt 07700 900735

Target Market(s)

Muslims

Font styles to use
Script

Colors

Designer to choose colors to be used in the design.

Requirements
Must have
• stylish calligraphy Arabic lettering of the dua requested above
• Size:
• Long 4" x 9.5"
Nice to have
• ottoman empire: Art theme

```html
<!DOCTYPE html>
<html lang="en">
<head>
<meta charset="utf-8">
<title>Wedding Invitation – Mehreen &amp; Bilal</title>
<link rel="stylesheet" href="https://fonts.googleapis.com/css2?family=Amiri&family=Great+Vibes&family=Parisienne&family=Crimson+Text&display=swap">
<style>
  :root{
    --rose:#ef5fa1;
    --blush:#fbebea;
    --magenta:#e6288a;
    --white:#ffffff;
    --script:"Great Vibes", cursive;
    --script-soft:"Parisienne", cursive;
    --serif:"Crimson Text", serif;
    --arabic:"Amiri", serif;
  }
  *{box-sizing:border-box;margin:0;padding:0}
  html,body{width:1055px;height:1200px;overflow:hidden;background:#fff}
  .canvas{position:relative;width:1055px;height:1200px}

  .card{position:absolute;top:73px;width:409px;height:922px;overflow:hidden;
        background:var(--card-bg);color:var(--card-ink);border:1px solid #ead6d8}
  .card--rose{left:69px;--card-bg:var(--rose);--card-ink:var(--white);
              --band-bg:var(--blush);--band-ink:var(--magenta);--ornament:var(--white)}
  .card--blush{left:557px;--card-bg:var(--blush);--card-ink:var(--magenta);
              --band-bg:var(--rose);--band-ink:var(--white);--ornament:var(--rose)}

  .line{position:absolute;left:0;width:100%;text-align:center;white-space:nowrap}

  .bismillah{position:absolute;left:106px;top:14px;width:196px;height:44px;
             border-radius:22px;background:var(--card-ink);opacity:.22}
  .verse-arabic{top:74px;font-family:var(--arabic);font-size:20.5px;line-height:32px;direction:rtl}
  .verse-english{top:110px;font-family:var(--serif);font-size:9.6px;line-height:16.5px;white-space:normal;padding:0 14px}

  .request{top:178px;font-family:var(--script-soft);font-size:16px;line-height:22px;white-space:normal}

  .band{position:absolute;left:0;top:320px;width:100%;height:250px;background:var(--band-bg);color:var(--band-ink)}
  .ornament{position:absolute;left:126px;width:164px;background:var(--ornament);opacity:.85}
  .ornament--top{top:252px;height:70px;border-radius:82px 82px 6px 6px}
  .ornament--bottom{top:568px;height:76px;border-radius:6px 6px 82px 82px}

  .name{font-family:var(--script);font-size:50px;line-height:60px}
  .name--bride{top:32px}
  .name--groom{top:150px}
  .parentage{font-family:var(--serif);font-size:13.5px;line-height:18px}
  .parentage--bride{top:83px}
  .parentage--groom{top:204px}
  .joiner{top:119px;font-family:var(--script);font-size:22px;line-height:30px}

  .details{top:654px;font-family:var(--serif);font-size:16.5px;line-height:24.5px;white-space:normal}

  .rsvp{position:absolute;left:12px;top:831px;font-family:var(--serif);font-size:12.5px;line-height:20.3px;list-style:none}
</style>
</head>
<body>
<main class="canvas">

  <article class="card card--rose">
    <div class="bismillah" role="img" aria-label="Bismillah in Arabic calligraphy"></div>
    <p class="line verse-arabic" lang="ar">أُولَـٰئِكَ يُجْزَوْنَ الْغُرْفَةَ بِمَا صَبَرُوا وَيُلَقَّوْنَ فِيهَا تَحِيَّةً وَسَلَامًا</p>
    <p class="line verse-english">Those will be awarded the Chamber for what they patiently endured, and they will be received therein with greetings and [words of] peace. (Quran Ch. 25. Verse 75.</p>
    <p class="line request">Mrs. Rubina Sohail wife of late Mr. Sohail Imran Qureshi<br>Cordially requests your company to grace the joyous occasion<br>of the wedding of their beloved daughter</p>
    <section class="band">
      <h1 class="line name name--bride">Mehreen Qureshi</h1>
      <p class="line parentage parentage--bride">Daughter of ( late) Mr Sohail Imran qureshi</p>
      <p class="line joiner">with</p>
      <h2 class="line name name--groom">Bilal Siddiqui</h2>
      <p class="line parentage parentage--groom">Son of Mr. Junaid Siddiqui &amp; Mrs Shazia Siddiqui</p>
    </section>
    <div class="ornament ornament--top" role="img" aria-label="Ottoman style scroll ornament"></div>
    <div class="ornament ornament--bottom" role="img" aria-label="Ottoman style scroll ornament"></div>
    <p class="line details">In sha’Allah<br>on Thursday 29th August 2019<br>at Velvet Orchard<br>12 Marlow Crescent, Croydon<br>CR7 2LP<br>Baraat Arrival: 6:30 pm</p>
    <ul class="rsvp">
      <li>RSVP</li>
      <li>Usman Qureshi 07700 900412</li>
      <li>Tariq Mehmood 07700 900583</li>
      <li>Faisal Butt 07700 900735</li>
    </ul>
  </article>

  <article class="card card--blush">
    <div class="bismillah" role="img" aria-label="Bismillah in Arabic calligraphy"></div>
    <p class="line verse-arabic" lang="ar">أُولَـٰئِكَ يُجْزَوْنَ الْغُرْفَةَ بِمَا صَبَرُوا وَيُلَقَّوْنَ فِيهَا تَحِيَّةً وَسَلَامًا</p>
    <p class="line verse-english">Those will be awarded the Chamber for what they patiently endured, and they will be received therein with greetings and [words of] peace. (Quran Ch. 25. Verse 75.</p>
    <p class="line request">Mrs. Rubina Sohail wife of late Mr. Sohail Imran Qureshi<br>Cordially requests your company to grace the joyous occasion<br>of the wedding of their beloved daughter</p>
    <section class="band">
      <h1 class="line name name--bride">Mehreen Qureshi</h1>
      <p class="line parentage parentage--bride">Daughter of ( late) Mr Sohail Imran qureshi</p>
      <p class="line joiner">with</p>
      <h2 class="line name name--groom">Bilal Siddiqui</h2>
      <p class="line parentage parentage--groom">Son of Mr. Junaid Siddiqui &amp; Mrs Shazia Siddiqui</p>
    </section>
    <div class="ornament ornament--top" role="img" aria-label="Ottoman style scroll ornament"></div>
    <div class="ornament ornament--bottom" role="img" aria-label="Ottoman style scroll ornament"></div>
    <p class="line details">In sha’Allah<br>on Thursday 29th August 2019<br>at Velvet Orchard<br>12 Marlow Crescent, Croydon<br>CR7 2LP<br>Baraat Arrival: 6:30 pm</p>
    <ul class="rsvp">
      <li>RSVP</li>
      <li>Usman Qureshi 07700 900412</li>
      <li>Tariq Mehmood 07700 900583</li>
      <li>Faisal Butt 07700 900735</li>
    </ul>
  </article>

</main>
</body>
</html>
```